A website for a Maltese Law Firm

Our law firm needs a website to further its business. The site should have a simple yet effective design. We would need the following sections: About us, Practice Areas, About Malta, Contact. These should be further split as follows:

About us: Our firm, Our values, What others say, Offices

Practice Areas: Crimimal, Citizenship & Residence, Harbour Passage Scheme, Criminal Defence, Civil Litigation, Arbitration and ADR, Commercial and Corporate, Media Law.

About Malta: just one section.

Contact: Just one section

We would also need a news feed at the front of the site to include latest news regarding our cases.

At the bottom we need a section for our Terms and a Privacy Statement.

Our logo is being attached.

Target Market(s)

All clients looking for legal assistance in Malta

Industry/Entity Type

Legal

Coding

Coded - Design and coding required

Number of Pages Required

1 page

Requirements
Must have
• It must be simple yet striking.

```html
<!DOCTYPE html>
<html lang="en">
<head>
<meta charset="utf-8">
<title>Mercieca &amp; Borg Advocates</title>
<link rel="stylesheet" href="https://fonts.googleapis.com/css2?family=Oswald:wght@400;500&family=Arimo:wght@400;700&family=Cinzel:wght@500&display=swap">
<style>
:root{
  --ink:#111;
  --topbar:#262626;
  --brown:#7a2f0c;
  --maroon:#7d0d0d;
  --accent-red:#8b1010;
  --row-num:#bdbbb6;
  --row-body:#e6e4df;
  --card-dark:#5c5654;
  --footer:#0e0806;
  --white:#fff;
}
*{box-sizing:border-box;margin:0;padding:0}
html,body{width:1200px;height:2466px;overflow:hidden}
body{position:relative;font-family:"Arimo",Arial,sans-serif;color:var(--ink);background:var(--white)}
.abs{position:absolute}
h1,h2,h3,h4{font-family:"Oswald","Arial Narrow",sans-serif;font-weight:400}

/* top bar */
.topbar{left:0;top:0;width:1200px;height:30px;background:var(--topbar);color:#ddd;font-size:10px;display:flex;align-items:center;padding:0 153px}
.topbar span{margin-right:18px;display:flex;align-items:center;gap:6px}
.social{margin-left:auto;display:flex;gap:4px}
.social i{display:block;width:13px;height:13px;border-radius:50%;background:#3d8fd0}
.social i:nth-child(2n){background:#e05a2a}
.social i:nth-child(3n){background:#2f6db3}

/* nav */
.nav{left:0;top:30px;width:1200px;height:69px;background:var(--white);display:flex;align-items:center;padding:0 153px;border-bottom:1px solid #ddd}
.brand{font-family:"Cinzel",serif;font-size:18px;font-weight:500;color:#222;letter-spacing:.5px;display:flex;align-items:center;gap:8px;width:219px}
.brand .mark{width:10px;height:10px;background:#222}
.menu{display:flex;list-style:none;font-size:11.5px}
.menu li{padding:0 15px;border-right:1px solid #e4e4e4;line-height:69px}
.menu li:first-child{padding-left:0}
.menu li:last-child{border-right:0}
.menu li.active{color:var(--maroon);border-right:0}
.search{left:1010px;top:48px}

/* hero */
.hero{left:0;top:99px;width:1200px;height:438px;background:radial-gradient(ellipse at 20% 60%,#c98a3e 0%,#7a3e14 35%,#3c1a0a 70%),linear-gradient(90deg,#4a2410,#a06636 60%,#5a2a12);background-blend-mode:overlay}
.hero-text{left:448px;top:205px;color:var(--white)}
.hero-text h1{font-size:37px;line-height:46px}
.hero-text p{margin-top:22px;font-size:13px;line-height:22.5px;width:420px}

/* services */
.services{left:0;top:537px;width:1200px;height:352px;background:var(--brown);color:var(--white)}
.services h2{position:absolute;top:18px;width:100%;text-align:center;font-size:28px;line-height:37px}
.svc{position:absolute;width:290px;display:flex;gap:22px}
.svc svg{flex:none}
.svc h3{font-size:18px;margin-top:-2px}
.svc p{font-size:12.5px;line-height:18px;margin-top:8px}

/* about & news */
.section-title{font-size:28px;color:#111}
.about{left:160px;top:916px;width:420px}
.about p{font-size:13px;line-height:22.5px;margin-top:14px}
.news{left:599px;top:916px;width:450px}
.news-grid{display:grid;grid-template-columns:218px 218px;column-gap:12px;margin-top:12px;list-style:none}
.news-item{display:flex;gap:12px;font-size:12.5px;line-height:18px;padding:5px 0 12px;border-bottom:1px solid #ddd;height:58px}
.news-item:nth-last-child(-n+2){border-bottom:0}

/* faq */
.faq-title{left:165px;top:1182px}
.faq{left:153px;top:1248px;width:680px;list-style:none}
.faq li{display:flex;margin-bottom:8px;background:var(--row-body)}
.faq .num{width:53px;background:var(--row-num);font-size:12px;padding-left:18px;padding-top:14px}
.faq .body{flex:1;padding:14px 20px;font-size:13px;position:relative}
.faq .body .sign{position:absolute;right:16px;top:11px;font-size:18px}
.faq .answer{color:var(--accent-red);font-size:10px;line-height:13px;margin-top:12px;padding-right:30px}
.faq li.closed{height:43px}

/* specialist */
.spec-title{left:854px;top:1182px}
.spec-photo{left:844px;top:1248px;width:209px;height:171px;background:linear-gradient(180deg,#eef0f2,#c9ccd0 60%,#3a3f48)}
.spec{left:846px;top:1437px;width:210px}
.spec h4{font-family:"Arimo",sans-serif;font-weight:400;font-size:18px}
.spec .role{font-size:13px;margin-top:6px}
.spec p{font-size:13px;line-height:18px;margin-top:6px}
.spec .links{display:flex;gap:10px;margin-top:14px}
.spec .links i{display:block;width:10px;height:10px;background:#111}

/* pricing */
.pricing{left:0;top:1646px;width:1200px;height:563px;background:var(--brown)}
.pricing h2{position:absolute;top:50px;width:100%;text-align:center;color:var(--white);font-size:38px}
.plan{position:absolute;top:130px;width:209px;height:382px;background:var(--white);text-align:center;padding-top:20px}
.plan h3{font-size:23px;color:var(--maroon)}
.plan .price{font-family:"Oswald",sans-serif;color:var(--maroon);font-size:26px;margin-top:2px}
.plan .price small{font-size:12px;vertical-align:top;line-height:26px}
.plan .price em{font-style:normal;font-size:15px;color:#555}
.plan .lead{font-size:13px;line-height:18px;margin-top:10px;padding:0 8px}
.plan ul{list-style:none;margin:12px 32px 0;font-size:10.5px}
.plan ul li{padding:8px 0;border-bottom:1px solid #ddd}
.plan ul li:last-child{border-bottom:0}
.plan .btn{display:inline-block;margin-top:14px;background:var(--maroon);color:var(--white);font-size:10.5px;padding:7px 12px;border-radius:5px}
.plan.featured{background:var(--card-dark)}
.plan.featured h3,.plan.featured .price,.plan.featured .price em,.plan.featured .lead,.plan.featured li{color:var(--white)}
.plan.featured .btn{background:var(--white);color:#222}

/* footer */
.footer{left:0;top:2209px;width:1200px;height:257px;background:var(--footer);color:var(--white)}
.fcol{position:absolute;top:42px;width:290px}
.fcol h4{font-family:"Arimo",sans-serif;font-weight:400;font-size:18px}
.fcol p{font-size:10.5px;line-height:18px;margin-top:14px}
.fline{left:0;top:172px;width:1200px;height:1px;background:#444}
.copy{left:161px;top:208px;font-size:10.5px}
.legal{left:470px;top:208px;font-size:10.5px;display:flex;gap:22px;list-style:none;color:#ccc}
.fsocial{left:860px;top:207px}
.totop{left:1019px;top:200px;width:28px;height:26px;background:#eee;border-radius:6px;display:flex;align-items:center;justify-content:center}
</style>
</head>
<body>

<div class="abs topbar">
  <span>Have any questions?</span>
  <span><svg width="10" height="10" viewBox="0 0 10 10"><path d="M2 0l2 2-1 1.5c.6 1.4 1.6 2.4 3 3L7.5 5.5l2 2L8 10C4 9.5.5 6 0 2z" fill="#ddd"/></svg>+356 2123 4567</span>
  <span><svg width="12" height="9" viewBox="0 0 12 9"><rect width="12" height="9" fill="#ddd"/><path d="M0 0l6 5 6-5" stroke="#262626" fill="none"/></svg>info@merciecaborg.mt</span>
  <div class="social"><i></i><i></i><i></i><i></i><i></i><i></i><i></i><i></i><i></i></div>
</div>

<header class="abs nav">
  <div class="brand"><span class="mark"></span>Mercieca &amp; Borg</div>
  <ul class="menu">
    <li class="active">Home</li><li>About us</li><li>Practice Areas</li><li>About Malta</li><li>Contact</li>
  </ul>
</header>
<svg class="abs search" width="20" height="20" viewBox="0 0 20 20"><circle cx="8" cy="8" r="6" stroke="#111" stroke-width="2.5" fill="none"/><path d="M12.5 12.5l6 6" stroke="#111" stroke-width="3"/></svg>

<section class="abs hero" role="img" aria-label="Courtroom scene with a wooden gavel and shelves of law books"></section>
<div class="abs hero-text">
  <h1>We know well how to do<br>&nbsp;a paper work</h1>
  <p>Vitae adipiscing turpis. Aenean ligula nibh, molestie id viverra a, dapibus at dolor. In iaculis viverra neque, ac eleifend ante lobortis id. In viverra ipsum ac eros tristique dignissim. Donec aliquam<br>velit vitae mi dictum.</p>
</div>

<section class="abs services">
  <h2>We offer you more than just<br>a typical law firm</h2>
  <div class="svc" style="left:153px;top:112px">
    <svg width="60" height="50" viewBox="0 0 60 50"><rect width="60" height="50" rx="6" fill="#a35a2c"/><path d="M22 14l5 5-3 3c2 4 5 7 9 9l3-3 5 5-4 4c-10-2-17-9-19-19z" fill="#fff"/></svg>
    <div><h3>Legal help</h3><p>Lorem ipsum dolor sit amet,<br>consectetuer adipiscing elit</p></div>
  </div>
  <div class="svc" style="left:448px;top:112px">
    <svg width="50" height="46" viewBox="0 0 50 46"><rect width="50" height="46" fill="#fff"/><path d="M8 36l10-10 8 6 14-16" stroke="#222" stroke-width="4" fill="none"/><circle cx="36" cy="34" r="7" fill="#222"/></svg>
    <div><h3>Fiscal advising</h3><p>Lorem ipsum dolor sit amet,<br>consectetuer adipiscing elit</p></div>
  </div>
  <div class="svc" style="left:746px;top:112px">
    <svg width="46" height="46" viewBox="0 0 46 46"><rect x="2" y="2" width="42" height="42" fill="none" stroke="#fff" stroke-width="3"/><rect x="9" y="9" width="28" height="28" fill="none" stroke="#fff" stroke-width="2"/><circle cx="23" cy="23" r="7" fill="#fff"/></svg>
    <div><h3>Qualified protection</h3><p>Lorem ipsum dolor sit amet,<br>consectetuer adipiscing elit</p></div>
  </div>
  <div class="svc" style="left:153px;top:225px">
    <svg width="52" height="50" viewBox="0 0 52 50"><ellipse cx="26" cy="28" rx="22" ry="16" fill="#fff"/><rect x="12" y="38" width="7" height="10" fill="#fff"/><rect x="32" y="38" width="7" height="10" fill="#fff"/><circle cx="26" cy="8" r="5" fill="#fff"/></svg>
    <div><h3>Financial advising</h3><p>Lorem ipsum dolor sit amet,<br>consectetuer adipiscing elit</p></div>
  </div>
  <div class="svc" style="left:448px;top:225px">
    <svg width="50" height="46" viewBox="0 0 50 46"><rect width="50" height="46" fill="#fff"/><g fill="none" stroke="#222" stroke-width="2.5"><ellipse cx="25" cy="12" rx="11" ry="4"/><path d="M14 12v22c0 2 5 4 11 4s11-2 11-4V12M14 19c0 2 5 4 11 4s11-2 11-4M14 27c0 2 5 4 11 4s11-2 11-4"/></g></svg>
    <div><h3>Vindication</h3><p>Lorem ipsum dolor sit amet,<br>consectetuer adipiscing elit</p></div>
  </div>
  <div class="svc" style="left:746px;top:225px">
    <svg width="50" height="50" viewBox="0 0 50 50"><circle cx="25" cy="25" r="25" fill="#6d6d6d"/><path d="M8 22l17-8 17 8-17 8z" fill="#fff"/><path d="M15 26v8c4 4 16 4 20 0v-8l-10 5z" fill="#fff"/></svg>
    <div><h3>Financial advising</h3><p>Lorem ipsum dolor sit amet,<br>consectetuer adipiscing elit</p></div>
  </div>
</section>

<section class="abs about">
  <h2 class="section-title">About us</h2>
  <p>Vitae adipiscing turpis. Aenean ligula nibh, molestie id viverra a, dapibus at dolor. In iaculis viverra neque, ac eleifend ante lobortis id. In viverra ipsum ac eros tristique dignissim. Donec aliquam<br>velit vitae mi dictum.</p>
  <p>Vitae adipiscing turpis. Aenean ligula nibh, molestie id viverra a, dapibus at dolor. In iaculis viverra neque, ac eleifend ante lobortis id. In viverra ipsum ac eros tristique dignissim. Donec aliquam<br>velit vitae mi dictum.</p>
</section>

<section class="abs news">
  <h2 class="section-title">Latest case news</h2>
  <ul class="news-grid">
    <li class="news-item"><svg width="12" height="16" viewBox="0 0 12 16"><path d="M6 0a6 6 0 0 1 6 6c0 4-6 10-6 10S0 10 0 6a6 6 0 0 1 6-6z" fill="#111"/><rect x="5" y="3" width="2" height="5" fill="#fff"/></svg><span>Appeal upheld in a long<br>commercial dispute</span></li>
    <li class="news-item"><svg width="12" height="16" viewBox="0 0 12 16"><path d="M6 0a6 6 0 0 1 6 6c0 4-6 10-6 10S0 10 0 6a6 6 0 0 1 6-6z" fill="#111"/><rect x="5" y="3" width="2" height="5" fill="#fff"/></svg><span>Client acquitted of all<br>charges in criminal trial</span></li>
    <li class="news-item"><svg width="12" height="16" viewBox="0 0 12 16"><path d="M6 0a6 6 0 0 1 6 6c0 4-6 10-6 10S0 10 0 6a6 6 0 0 1 6-6z" fill="#111"/><rect x="5" y="3" width="2" height="5" fill="#fff"/></svg><span>Residence permits granted<br>to three investor families</span></li>
    <li class="news-item"><svg width="12" height="16" viewBox="0 0 12 16"><path d="M6 0a6 6 0 0 1 6 6c0 4-6 10-6 10S0 10 0 6a6 6 0 0 1 6-6z" fill="#111"/><rect x="5" y="3" width="2" height="5" fill="#fff"/></svg><span>Arbitration award settled<br>for shipping company</span></li>
    <li class="news-item"><svg width="12" height="16" viewBox="0 0 12 16"><path d="M6 0a6 6 0 0 1 6 6c0 4-6 10-6 10S0 10 0 6a6 6 0 0 1 6-6z" fill="#111"/><rect x="5" y="3" width="2" height="5" fill="#fff"/></svg><span>Media law case closes with<br>full public apology</span></li>
    <li class="news-item"><svg width="12" height="16" viewBox="0 0 12 16"><path d="M6 0a6 6 0 0 1 6 6c0 4-6 10-6 10S0 10 0 6a6 6 0 0 1 6-6z" fill="#111"/><rect x="5" y="3" width="2" height="5" fill="#fff"/></svg><span>Harbour Passage Scheme<br>rules updated this month</span></li>
  </ul>
</section>

<h2 class="abs section-title faq-title">Latest questions and answers</h2>
<ol class="abs faq">
  <li style="height:140px"><div class="num">1</div><div class="body">Donec aliquam velit vitae mi dictum.<span class="sign">+</span>
    <p class="answer">Lorem ipsum dolor sit amet, consectetuer adipiscing elit.Lorem ipsum dolor sit amet, consectetuer adipiscing elit Lorem ipsum dolor sit amet, consectetuer adipiscing elit.Lorem ipsum dolor sit amet, consectetuer adipiscing elit</p>
    <p class="answer">Lorem ipsum dolor sit amet, consectetuer adipiscing elit.Lorem ipsum dolor sit amet, consectetuer adipiscing elit<br>Lorem ipsum dolor sit amet, consectetuer adipiscing elit.Lorem ipsum dolor sit amet, consectetuer adipiscing elit</p></div></li>
  <li class="closed"><div class="num">2</div><div class="body">Donec aliquam velit vitae mi dictum.<span class="sign">&minus;</span></div></li>
  <li class="closed"><div class="num">3</div><div class="body">Donec aliquam velit vitae mi dictum.<span class="sign">&minus;</span></div></li>
  <li class="closed"><div class="num">4</div><div class="body">Donec aliquam velit vitae mi dictum.<span class="sign">&minus;</span></div></li>
  <li class="closed"><div class="num">5</div><div class="body">Donec aliquam velit vitae mi dictum.<span class="sign">&minus;</span></div></li>
</ol>

<h2 class="abs section-title spec-title">Specialist</h2>
<div class="abs spec-photo" role="img" aria-label="Portrait photo of the specialist lawyer in a suit"></div>
<div class="abs spec">
  <h4>Martin Ellul</h4>
  <div class="role">Lawyer</div>
  <p>Lorem ipsum dolor sit amet,<br>consectetuer adipiscing elit</p>
  <div class="links"><i></i><i></i><i></i><i></i></div>
</div>

<section class="abs pricing">
  <h2>Choose your monthly plan</h2>
  <div class="plan" style="left:153px">
    <h3>Basic</h3><div class="price"><small>$</small> 12 / <em>monthly</em></div>
    <p class="lead">Lorem ipsum dolor sit amet,<br>consectetuer adipiscing elit</p>
    <ul><li>5 cases at least</li><li>Unlimited meetings</li><li>30 hours in court</li><li>Professional vindication</li><li>10 customers at time</li></ul>
    <span class="btn">sign up now</span>
  </div>
  <div class="plan featured" style="left:380px">
    <h3>Standard</h3><div class="price"><small>$</small> 24 / <em>monthly</em></div>
    <p class="lead">Lorem ipsum dolor sit amet,<br>consectetuer adipiscing elit</p>
    <ul><li>5 cases at least</li><li>Unlimited meetings</li><li>30 hours in court</li><li>Professional vindication</li><li>10 customers at time</li></ul>
    <span class="btn">sign up now</span>
  </div>
  <div class="plan" style="left:611px">
    <h3>Business</h3><div class="price"><small>$</small> 29/ <em>monthly</em></div>
    <p class="lead">Lorem ipsum dolor sit amet,<br>consectetuer adipiscing elit</p>
    <ul><li>5 cases at least</li><li>Unlimited meetings</li><li>30 hours in court</li><li>Professional vindication</li><li>10 customers at time</li></ul>
    <span class="btn">sign up now</span>
  </div>
  <div class="plan" style="left:839px">
    <h3>Professional</h3><div class="price"><small>$</small> 39/ <em>monthly</em></div>
    <p class="lead">Lorem ipsum dolor sit amet,<br>consectetuer adipiscing elit</p>
    <ul><li>5 cases at least</li><li>Unlimited meetings</li><li>30 hours in court</li><li>Professional vindication</li><li>10 customers at time</li></ul>
    <span class="btn">sign up now</span>
  </div>
</section>

<footer class="abs footer">
  <div class="fcol" style="left:161px"><h4>Bibendum auctor</h4><p>Sed ut imperdiet nisi. Proin condimentum fermentum nunc. Etiam pharetra, erat sed fermentum feugiat, velit mauris egestas quam, ut aliquam massa nisl quis neque.</p></div>
  <div class="fcol" style="left:472px"><h4>Bibendum auctor</h4><p>Sed ut imperdiet nisi. Proin condimentum fermentum nunc. Etiam pharetra, erat sed fermentum feugiat, velit mauris egestas quam, ut aliquam massa nisl quis neque.</p></div>
  <div class="fcol" style="left:775px"><h4>Bibendum auctor</h4><p>Sed ut imperdiet nisi. Proin condimentum fermentum nunc. Etiam pharetra, erat sed fermentum feugiat, velit mauris egestas quam, ut aliquam massa nisl quis neque.</p></div>
  <div class="abs fline"></div>
  <div class="abs copy">&copy; 2016 Mercieca &amp; Borg. All Rights Reserved.</div>
  <ul class="abs legal"><li>Terms</li><li>Privacy Statement</li></ul>
  <div class="abs social fsocial"><i></i><i></i><i></i><i></i><i></i><i></i><i></i><i></i><i></i></div>
  <div class="abs totop"><svg width="12" height="8" viewBox="0 0 12 8"><path d="M1 7l5-5 5 5" stroke="#111" stroke-width="2.5" fill="none"/></svg></div>
</footer>

</body>
</html>
```